Brindlecove Business Card

Looking for a new business Card layout for our company, brindlecove.

Logo Text

Standard Business Card , Name, email, phone, website. www.brindlecove-example.com

```html
<!DOCTYPE html>
<html lang="en">
<head>
<meta charset="utf-8">
<title>Brindlecove Business Card</title>
<link rel="stylesheet" href="https://fonts.googleapis.com/css2?family=Montserrat:wght@800&family=Roboto:wght@300;400&family=Comfortaa:wght@700&display=swap">
<style>
  :root {
    --backdrop: #5b5c5e;
    --card-dark: #1f1f20;
    --card-light: #ffffff;
    --brand-blue: #47b5dc;
    --slate: #56627a;
    --text-grey: #4f5566;
    --white: #ffffff;
  }
  * { margin: 0; padding: 0; box-sizing: border-box; }
  html, body { width: 1200px; height: 1124px; overflow: hidden; }
  body {
    background: var(--backdrop);
    font-family: "Roboto", Arial, sans-serif;
    position: relative;
  }
  .card {
    position: absolute;
    left: 160px;
    width: 880px;
    height: 503px;
    box-shadow: 0 10px 24px rgba(0,0,0,0.35);
  }
  .card-back { top: 30px; background: var(--card-dark); }
  .card-front { top: 591px; background: var(--card-light); }

  .back-brand {
    position: absolute;
    left: 0; right: 0; top: 200px;
    display: flex; align-items: center; justify-content: center; gap: 18px;
  }
  .brand-dot {
    width: 26px; height: 26px; border-radius: 50%;
    background: var(--brand-blue);
  }
  .brand-name {
    font-family: "Montserrat", Arial, sans-serif;
    font-weight: 800;
    text-transform: uppercase;
    letter-spacing: 1px;
    color: var(--brand-blue);
  }
  .back-brand .brand-name { font-size: 64px; }
  .back-website {
    position: absolute;
    left: 0; right: 0; top: 300px;
    text-align: center;
    font-weight: 300;
    font-size: 22px;
    color: var(--white);
    letter-spacing: 0.5px;
  }

  .front-brand {
    position: absolute; left: 60px; top: 50px;
  }
  .front-brand .brand-name { font-size: 38px; color: var(--slate); }
  .holder {
    position: absolute; right: 70px; top: 110px; text-align: right;
  }
  .holder-name {
    font-family: "Comfortaa", Arial, sans-serif;
    font-weight: 700;
    font-size: 32px;
    color: var(--brand-blue);
  }
  .holder-role {
    font-size: 26px;
    font-weight: 300;
    color: var(--text-grey);
    margin-top: 4px;
  }
  .address {
    position: absolute; left: 110px; top: 215px;
    font-size: 24px; font-weight: 300; line-height: 32px;
    color: var(--text-grey);
  }
  .contacts {
    position: absolute; left: 80px; top: 300px;
    list-style: none;
  }
  .contacts li {
    display: flex; align-items: center; gap: 16px;
    font-size: 25px; font-weight: 300; color: var(--text-grey);
    height: 38px;
  }
  .contacts svg { width: 20px; height: 20px; flex: none; }
  .accent { color: var(--brand-blue); }
</style>
</head>
<body>
  <section class="card card-back">
    <div class="back-brand">
      <span class="brand-dot"></span>
      <span class="brand-name">Brindlecove</span>
    </div>
    <p class="back-website">www.brindlecove-example.com</p>
  </section>

  <section class="card card-front">
    <div class="front-brand"><span class="brand-name">Brindlecove</span></div>
    <div class="holder">
      <p class="holder-name">Quentin Marsh</p>
      <p class="holder-role">Manager</p>
    </div>
    <p class="address">Your address<br>city, state, ZIP 0000</p>
    <ul class="contacts">
      <li>
        <svg viewBox="0 0 24 24" aria-hidden="true"><path fill="#47b5dc" d="M6.6 10.8a15 15 0 0 0 6.6 6.6l2.2-2.2c.3-.3.7-.4 1-.2 1.1.4 2.3.6 3.6.6.6 0 1 .4 1 1V20c0 .6-.4 1-1 1A17 17 0 0 1 3 4c0-.6.4-1 1-1h3.5c.6 0 1 .4 1 1 0 1.3.2 2.5.6 3.6.1.3 0 .7-.2 1z"/></svg>
        555-014-7380
      </li>
      <li>
        <svg viewBox="0 0 24 24" aria-hidden="true"><rect x="2.5" y="5" width="19" height="14" rx="1.5" fill="none" stroke="#47b5dc" stroke-width="2"/><path d="M3 6l9 7 9-7" fill="none" stroke="#47b5dc" stroke-width="2"/></svg>
        hello@brindlecove-example.com
      </li>
      <li>
        <svg viewBox="0 0 24 24" aria-hidden="true"><g fill="none" stroke="#47b5dc" stroke-width="1.6"><circle cx="12" cy="12" r="9.5"/><ellipse cx="12" cy="12" rx="4" ry="9.5"/><path d="M2.5 12h19M4 7h16M4 17h16"/></g></svg>
        <span>www.<span class="accent">brindlecove-example</span>.com</span>
      </li>
    </ul>
  </section>
</body>
</html>
```